Velmora Partners - website for real estate investment company

Create a bold, modern website that reflects Velmora’s success, professionalism, and credibility.
The design must stand out while maintaining a polished, corporate tone. (bold, but understated)
The client just created a new logo, and the website design must be in sync with the logo design. Information about the logo colors, fonts, and message are in the attached design brief.
Updates

Target Market(s)

b2b: banks, brokers, institutional partners, vendors, and property sellers.

Industry/Entity Type

real estate investment company

Number of Pages Required

1 page

Font styles to use
Sans Serif

Colors

Designer to choose colors to be used in the design.

Requirements
Must have
• 1. homepage design (psd) 2. a top banner image (psd) for a default inner page
Nice to have
• please see attached design brief
Should not have

```html
<!DOCTYPE html>
<html lang="en">
<head>
<meta charset="utf-8">
<title>Velmora Partners</title>
<link href="https://fonts.googleapis.com/css2?family=Roboto:wght@400;500;700;900&display=swap" rel="stylesheet">
<style>
:root{
  --red:#e01f2b;
  --red-soft:rgba(224,31,43,.72);
  --ink:#3b3b3f;
  --text:#5a5a5e;
  --muted:#707075;
  --blush:#fff5f5;
  --fog:#e6e6e9;
  --footer:#eeeef3;
  --bar:#3a3a3e;
  --white:#ffffff;
}
*{box-sizing:border-box;margin:0;padding:0}
html,body{width:1200px;height:3162px;overflow:hidden}
body{font-family:'Roboto',sans-serif;color:var(--text);background:var(--white);position:relative}
.abs{position:absolute}
.btn{position:absolute;background:var(--red);color:var(--white);font-size:13px;font-weight:500;display:flex;align-items:center;justify-content:center;border-radius:4px;text-transform:uppercase}
.eyebrow{position:absolute;color:var(--red);font-size:18px;display:flex;align-items:flex-end}
.eyebrow::after{content:"";display:block;width:86px;height:1px;background:var(--red);margin-left:2px;margin-bottom:4px}
.title{position:absolute;font-weight:700;color:var(--ink);font-size:54px;letter-spacing:.5px;line-height:1}
.body-copy{position:absolute;font-size:16px;line-height:23px;color:var(--text)}

/* header + hero */
.hero{position:absolute;left:0;top:0;width:1200px;height:742px;overflow:hidden}
.hero-photo{position:absolute;inset:0;background:linear-gradient(180deg,#d8dde3 0%,#b7c1cc 28%,#7d8ea2 55%,#4c5c6e 80%,#2f3b45 100%)}
.hero-slant{position:absolute;left:0;top:0}
.logo{position:absolute;font-weight:900;color:var(--ink);letter-spacing:0;white-space:nowrap;line-height:1}
.nav{position:absolute;left:334px;top:18px;width:515px;height:32px;border-bottom:1.5px solid #55585c;display:flex;gap:29px;font-size:12.5px;color:#3f4145;text-transform:uppercase}
.nav span.active{color:var(--red)}
.hero h1{position:absolute;left:175px;top:182px;color:var(--white);font-size:54px;font-weight:700;line-height:62px;letter-spacing:.5px}
.hero p{position:absolute;left:175px;top:384px;width:470px;color:var(--white);font-size:14.5px;line-height:27px}

/* story */
.story-photo{position:absolute;left:147px;top:811px;width:323px;height:335px;background:linear-gradient(135deg,#e9d3b5 0%,#b59673 35%,#6f6a66 65%,#cfd2cf 100%)}

/* strategy */
.strategy{position:absolute;left:0;top:1190px;width:1200px;height:463px;background:var(--blush)}
.step{position:absolute;left:663px;width:374px;background:var(--white);padding:22px 0 0 26px;font-size:12px;line-height:23px;color:var(--text)}
.step h4{font-size:13.5px;font-weight:500;color:var(--ink);line-height:18px;margin-bottom:2px}
.step .num{position:absolute;left:0;top:0}

/* portfolio */
.portfolio{position:absolute;left:0;top:1653px;width:1200px;height:599px;background:var(--fog)}
.service{position:absolute;top:206px;width:220px;height:252px;background:var(--white);border-radius:6px;text-align:center}
.service.featured{border:2px solid var(--red)}
.service .icon{width:60px;height:56px;margin:16px auto 0;border-radius:8px;background:linear-gradient(135deg,#f4b63c,#3a7cc0)}
.service h3{font-size:18px;font-weight:400;color:var(--ink);margin-top:18px;letter-spacing:.3px;white-space:nowrap}
.service.featured h3{color:var(--red)}
.service p{font-size:11.5px;line-height:23px;color:var(--text);margin:10px 10px 0}

/* stats */
.stats{position:absolute;left:0;top:2252px;width:1200px;height:101px;background:var(--red);color:var(--white);font-weight:700}
.stat{position:absolute}
.divider{position:absolute;top:25px;width:1px;height:52px;background:rgba(255,255,255,.4)}

/* contact */
.contact{position:absolute;left:0;top:2353px;width:1200px;height:506px;background:linear-gradient(180deg,#6e7176 0%,#5a5d62 60%,#4a4c50 100%)}
.field{position:absolute;background:var(--white);border-radius:2px;font-size:12px;color:#6a6a6e;padding-left:30px;display:flex;align-items:center;text-transform:uppercase}
.tower{position:absolute;left:671px;top:83px;width:388px;height:347px;background:linear-gradient(180deg,#e6ebef 0%,#b8c9d8 35%,#3f6c97 65%,#2f4d3a 100%)}

/* footer */
.footer{position:absolute;left:0;top:2859px;width:1200px;height:258px;background:var(--footer)}
.col-head{position:absolute;color:var(--red);font-size:14px;text-transform:uppercase}
.col-link{position:absolute;font-size:13px;color:#5d5d62}
.social{position:absolute;top:119px;width:24px;height:24px;border-radius:50%;background:#1e1e22}
.social.first{background:var(--red)}
.legal{position:absolute;left:0;top:3117px;width:1200px;height:45px;background:var(--bar);color:#e8e8ea;font-size:12px;display:flex;align-items:center;justify-content:center}
</style>
</head>
<body>

<section class="hero">
  <div class="hero-photo" role="img" aria-label="Photograph of glass office towers in a city skyline"></div>
  <svg class="hero-slant" width="1200" height="742" viewBox="0 0 1200 742">
    <polygon points="120,101 583,101 120,638" fill="var(--red-soft)"/>
    <polygon points="0,720 1200,734 1200,742 0,742" fill="var(--red)"/>
    <polygon points="0,722 700,730 1200,738 1200,742 0,742" fill="var(--white)"/>
  </svg>
  <div class="logo" style="left:120px;top:16px;font-size:38px">VELMORA</div>
  <nav class="nav">
    <span class="active">Home</span><span>Our Story</span><span>Investment Strategy</span><span>Our Portfolio</span><span>Contact</span>
  </nav>
  <div class="btn" style="left:969px;top:12px;width:111px;height:37px">Get Started</div>
  <h1>EXPERIENCE<br>STRATEGY<br>VISION</h1>
  <p>Velmora Partners is a vertically integrated real estate investment firm with a proven four-decade track record. We acquire, reposition, and operate high-performing assets across multiple sectors — always with a focus on exceptional, risk-adjusted returns.</p>
  <div class="btn" style="left:175px;top:515px;width:123px;height:37px">Contact Us</div>
</section>

<section class="story">
  <svg class="abs" style="left:384px;top:786px" width="106" height="124"><polygon points="0,0 106,0 106,124" fill="var(--red-soft)"/></svg>
  <div class="story-photo" role="img" aria-label="Photograph of hands over a contract beside a small model house"></div>
  <svg class="abs" style="left:384px;top:786px" width="106" height="124"><polygon points="20,0 106,0 106,124 86,96 86,25" fill="var(--red)" opacity=".55"/></svg>
  <div class="eyebrow" style="left:589px;top:795px">About us</div>
  <div class="title" style="left:587px;top:826px">OUR STORY</div>
  <div class="body-copy" style="left:589px;top:888px;width:490px">Lorem Ipsum is simply dummy text of the printing and typesetting industry. Lorem Ipsum has been the industry's standard dummy text ever since the 1500s, when an unknown printer took a galley of type and scrambled it to make a type specimen book. It has survived not only five centuries, but also the leap into electronic typesetting, remaining<br>Lorem Ipsum is simply dummy text of the printing and typesetting</div>
  <div class="btn" style="left:589px;top:1100px;width:124px;height:40px">Know More</div>
  <svg class="abs" style="left:0;top:1170px" width="530" height="22"><polygon points="0,0 522,18 0,20" fill="#4a4a4e"/></svg>
</section>

<section class="strategy">
  <div class="eyebrow" style="left:120px;top:68px">Investment</div>
  <div class="title" style="left:119px;top:98px">STRATEGY</div>
  <div class="body-copy" style="left:120px;top:170px;width:390px">Lorem Ipsum is simply dummy text of the printing and typesetting industry. Lorem Ipsum has been the industry's standard dummy text ever since the 1500s, when an unknown printer took also the leap into electronic typesetting, remaining</div>
  <div class="btn" style="left:121px;top:323px;width:126px;height:39px">Know More</div>

  <div class="step" style="top:96px;height:86px">
    <svg class="num" width="52" height="49"><polygon points="0,0 52,0 0,49" fill="#3f3f43"/><text x="8" y="22" fill="#fff" font-size="20" font-family="Roboto,sans-serif">1</text></svg>
    <h4>Buy and Hold — The Timeless Approach</h4>Lorem Ipsum is simply dummy text of the printing and<br>typesetting industry. Lorem Ipsum has been the industry's
  </div>
  <div class="step" style="top:197px;height:85px">
    <svg class="num" width="52" height="49"><polygon points="0,0 52,0 0,49" fill="#3f3f43"/><text x="8" y="22" fill="#fff" font-size="20" font-family="Roboto,sans-serif">2</text></svg>
    <h4>Invest in Under-Construction Projects</h4>Lorem Ipsum is simply dummy text of the printing and<br>typesetting industry. Lorem Ipsum has been the industry's
  </div>
  <div class="step" style="top:297px;height:87px">
    <svg class="num" width="52" height="49"><polygon points="0,0 52,0 0,49" fill="#3f3f43"/><text x="8" y="22" fill="#fff" font-size="20" font-family="Roboto,sans-serif">3</text></svg>
    <h4>Invest in Rental Properties with High Yield Potential</h4>Lorem Ipsum is simply dummy text of the printing and
  </div>
</section>

<section class="portfolio">
  <div class="abs" style="left:467px;top:75px;width:266px;text-align:center;color:var(--red);font-size:18px">
    <span style="display:inline-block;width:86px;height:1px;background:var(--red);vertical-align:4px"></span>What we do<span style="display:inline-block;width:86px;height:1px;background:var(--red);vertical-align:4px"></span>
  </div>
  <div class="title" style="left:0;width:1200px;text-align:center;top:111px">OUR PORTFOLIO</div>

  <div class="service" style="left:120px">
    <div class="icon" role="img" aria-label="Icon of a hand holding coins"></div>
    <h3>INVESTMENT</h3>
    <p>Lorem Ipsum is simply dummy text of the printing and typesetting industry. Lorem Ipsum has been the industry's standard dummy text ever</p>
  </div>
  <div class="service featured" style="left:367px;width:222px">
    <div class="icon" role="img" aria-label="Icon of a building under construction with a crane"></div>
    <h3>CUNTRUCTION</h3>
    <p>Lorem Ipsum is simply dummy text of the printing and typesetting industry. Lorem Ipsum has been the industry's standard dummy text ever</p>
  </div>
  <div class="service" style="left:615px">
    <div class="icon" role="img" aria-label="Icon of a land plot with a sale sign"></div>
    <h3>LAND SALES</h3>
    <p>Lorem Ipsum is simply dummy text of the printing and typesetting industry. Lorem Ipsum has been the industry's standard dummy text ever</p>
  </div>
  <div class="service" style="left:861px">
    <div class="icon" role="img" aria-label="Icon of a project manager with gears"></div>
    <h3>PROJECT MANAGEMENT</h3>
    <p>Lorem Ipsum is simply dummy text of the printing and typesetting industry. Lorem Ipsum has been the industry's standard dummy text ever</p>
  </div>

  <div class="btn" style="left:540px;top:519px;width:121px;height:36px">View More</div>
</section>

<section class="stats">
  <div class="stat" style="left:120px;top:22px"><div style="font-size:34px;line-height:34px">1989</div><div style="font-size:20px;line-height:24px">FOUNDED</div></div>
  <div class="divider" style="left:310px"></div>
  <div class="stat" style="left:430px;top:10px"><div style="font-size:34px;line-height:36px">23,000+</div><div style="font-size:20px;line-height:24px">MULTIFAMILY<br>&amp; HEALTHCARE UNITS</div></div>
  <div class="divider" style="left:753px"></div>
  <div class="stat" style="left:869px;top:12px"><div style="font-size:34px;line-height:36px">$300+</div><div style="font-size:20px;line-height:24px">MILLION INVESTED IN<br>RENOVATIONS</div></div>
</section>

<section class="contact" role="img" aria-label="Muted photograph of city towers behind the contact form">
  <div class="abs" style="left:120px;top:72px;color:var(--white);font-size:18px;display:flex;align-items:flex-end">Get in touch with us<span style="display:block;width:56px;height:1px;background:var(--white);margin:0 0 4px 2px"></span></div>
  <div class="abs" style="left:120px;top:100px;color:var(--white);font-size:38px;font-weight:700">CONTACT US</div>
  <div class="field" style="left:120px;top:156px;width:217px;height:41px">First Name</div>
  <div class="field" style="left:358px;top:156px;width:217px;height:41px">Last Name</div>
  <div class="field" style="left:120px;top:217px;width:217px;height:41px">Email Address</div>
  <div class="field" style="left:358px;top:217px;width:217px;height:41px">Phone Number</div>
  <div class="field" style="left:120px;top:280px;width:455px;height:80px;align-items:flex-start;padding-top:24px">Leave Message</div>
  <div class="btn" style="left:120px;top:383px;width:127px;height:33px;border-radius:3px">Send Message</div>
  <div class="tower" role="img" aria-label="Photograph of a modern glass office tower against the sky"></div>
</section>

<footer class="footer">
  <div class="logo" style="left:120px;top:46px;font-size:38px">VELMORA</div>
  <div class="social first" style="left:122px" aria-label="Video channel"></div>
  <div class="social" style="left:168px" aria-label="Social page"></div>
  <div class="social" style="left:215px" aria-label="Professional network"></div>
  <div class="social" style="left:260px" aria-label="Microblog"></div>

  <div class="col-head" style="left:368px;top:42px">Main Links</div>
  <div class="col-link" style="left:368px;top:73px">Our Story</div>
  <div class="col-link" style="left:368px;top:103px">Investment Strategy</div>
  <div class="col-link" style="left:368px;top:133px">Our Portfolio</div>
  <div class="col-link" style="left:368px;top:163px">Contact</div>

  <div class="col-head" style="left:577px;top:42px">Contact Us</div>
  <svg class="abs" style="left:577px;top:72px" width="22" height="26" viewBox="0 0 22 26" fill="none" stroke="#3b3b3f" stroke-width="1.4"><path d="M11 22 C5 15 4 12 4 9.5 A7 7 0 0 1 18 9.5 C18 12 17 15 11 22Z"/><circle cx="11" cy="9.5" r="2.6"/><path d="M6 21 Q11 25 16 21"/></svg>
  <div class="col-link" style="left:627px;top:71px;width:190px;line-height:17px">Address: 240 Harbor Ave,<br>Elmwood, NJ 07010</div>
  <svg class="abs" style="left:577px;top:130px" width="24" height="24" viewBox="0 0 24 24" fill="none" stroke="#3b3b3f" stroke-width="1.4"><path d="M5 3 L9 3 L10.5 8 L8 10 C9.5 13 11 14.5 14 16 L16 13.5 L21 15 L21 19 C21 20 20 21 19 21 C10 20.5 3.5 14 3 5 C3 4 4 3 5 3Z"/><path d="M14 3 A7 7 0 0 1 21 10"/><path d="M14 6.5 A3.5 3.5 0 0 1 17.5 10"/></svg>
  <div class="col-link" style="left:627px;top:135px">Phone: (555) 014-2287</div>
  <svg class="abs" style="left:579px;top:180px" width="24" height="18" viewBox="0 0 24 18" fill="none" stroke="#3b3b3f" stroke-width="1.4"><rect x="1" y="1" width="22" height="16"/><path d="M1 1 L12 10 L23 1"/><path d="M1 17 L9 8 M23 17 L15 8"/></svg>
  <div class="col-link" style="left:627px;top:180px">info@velmora.com</div>

  <div class="col-head" style="left:861px;top:42px">Other Links</div>
  <div class="col-link" style="left:861px;top:73px">Resources</div>
  <div class="col-link" style="left:861px;top:103px">Support</div>
  <div class="col-link" style="left:861px;top:133px">Reviews</div>
  <div class="col-link" style="left:861px;top:163px">Term and Condition</div>
</footer>

<div class="legal">COPY RIGHT © 2025&nbsp; VELMORA.COM . ALL RIGHTS RESERVED.</div>

</body>
</html>
```